Modern card design needed for building development company

We are looking for a sharp modern new look for our business cards.
We are a New Zealand based company called TKV Ventures NZ LTD that specialises in subdividing large sections, housing and commercial buildings.
We have attached a photo of the current logo and would like to see it improved somehow as it looks a bit dated.
We are open to any colours.

Target Market(s)

Investors, Property buyers

Industry/Entity Type

Investment

Contact Information for Business Card

TKV VENTURES NZ LTD
www.tkvventuresnz.co.nz

Howard Pennick
Phone +64 21 843 192
Email hdpennick@fernmail.co.nz

Font styles to use
Serif
Sans Serif

Colors
0792cd
33a6d7
85cae6
6b449b
886aae
f04a50
ec1f27
f37122
f68d4d

Requirements
Must have
• Please try and make the logo more modern or if you have a similar one we would like to see it.

```html
<!DOCTYPE html>
<html lang="en">
<head>
<meta charset="utf-8">
<title>TKV Ventures NZ LTD — Business Card</title>
<link rel="stylesheet" href="https://fonts.googleapis.com/css2?family=Michroma&family=Open+Sans:wght@400;700&display=swap">
<style>
  :root {
    --backdrop: #3b332e;
    --violet: #5f3b92;
    --violet-band: #6a45a0;
    --violet-deep: #4c2a80;
    --paper: #ffffff;
    --ink: #2b2b2b;
  }
  html, body {
    margin: 0;
    padding: 0;
    width: 1200px;
    height: 1200px;
    overflow: hidden;
    background: var(--backdrop);
  }
  .canvas {
    position: relative;
    width: 1200px;
    height: 1200px;
  }
  .card {
    position: absolute;
    left: 160px;
    width: 880px;
    height: 503px;
    overflow: hidden;
    box-shadow: 0 10px 30px rgba(0,0,0,0.35);
  }
  .card--front {
    top: 70px;
    background: linear-gradient(135deg, #573486 0%, var(--violet) 55%, #6a44a0 100%);
    display: flex;
    align-items: center;
    justify-content: center;
  }
  .card--back {
    top: 627px;
    background: var(--paper);
  }
  .wordmark {
    margin: 0;
    font-family: "Open Sans", sans-serif;
    font-weight: 700;
    text-transform: uppercase;
    line-height: 1.05;
    letter-spacing: 1px;
    text-align: center;
  }
  .card--front .wordmark {
    color: var(--paper);
    font-size: 52px;
    width: 420px;
  }
  .card--back .wordmark {
    position: absolute;
    left: 70px;
    top: 130px;
    width: 380px;
    color: var(--violet-band);
    font-size: 50px;
  }
  .contact {
    position: absolute;
    left: 500px;
    top: 172px;
  }
  .contact__name {
    margin: 0 0 16px;
    font-family: "Michroma", sans-serif;
    font-weight: 400;
    font-size: 24px;
    letter-spacing: 1px;
    color: var(--violet-band);
    text-transform: uppercase;
  }
  .contact__list {
    list-style: none;
    margin: 0;
    padding: 0;
  }
  .contact__item {
    display: flex;
    align-items: center;
    gap: 12px;
    margin-bottom: 8px;
    font-family: "Open Sans", sans-serif;
    font-size: 17px;
    color: var(--ink);
  }
  .contact__icon {
    width: 20px;
    height: 20px;
    flex: none;
  }
  .band {
    position: absolute;
    left: 0;
    bottom: 0;
    width: 880px;
    height: 110px;
  }
</style>
</head>
<body>
<main class="canvas">

  <section class="card card--front" aria-label="Card front">
    <h1 class="wordmark">TKV Ventures NZ LTD</h1>
  </section>

  <section class="card card--back" aria-label="Card back">
    <h2 class="wordmark">TKV Ventures NZ LTD</h2>

    <div class="contact">
      <p class="contact__name">Howard Pennick</p>
      <ul class="contact__list">
        <li class="contact__item">
          <svg class="contact__icon" viewBox="0 0 20 20" aria-hidden="true">
            <circle cx="10" cy="10" r="10" fill="#6a45a0"/>
            <path d="M7 5.5l1.6 0 .8 2.4-1.1.9c.6 1.3 1.6 2.3 2.9 2.9l.9-1.1 2.4.8v1.6c0 .6-.5 1-1.1 1C9 14 6 11 6 6.6c0-.6.4-1.1 1-1.1z" fill="#fff"/>
          </svg>
          <span>+64 21 843 192</span>
        </li>
        <li class="contact__item">
          <svg class="contact__icon" viewBox="0 0 20 20" aria-hidden="true">
            <circle cx="10" cy="10" r="10" fill="#6a45a0"/>
            <rect x="5" y="6.5" width="10" height="7" rx="1" fill="#fff"/>
            <path d="M5.3 7l4.7 3.5L14.7 7" fill="none" stroke="#6a45a0" stroke-width="1"/>
          </svg>
          <span>hdpennick@fernmail.co.nz</span>
        </li>
        <li class="contact__item">
          <svg class="contact__icon" viewBox="0 0 20 20" aria-hidden="true">
            <circle cx="10" cy="10" r="10" fill="#6a45a0"/>
            <g fill="none" stroke="#fff" stroke-width="1">
              <circle cx="10" cy="10" r="5"/>
              <ellipse cx="10" cy="10" rx="2.2" ry="5"/>
              <line x1="5" y1="10" x2="15" y2="10"/>
            </g>
          </svg>
          <span>www.tkvventuresnz.co.nz</span>
        </li>
      </ul>
    </div>

    <svg class="band" viewBox="0 0 880 110" aria-hidden="true">
      <polygon points="0,40 660,0 660,110 0,110" fill="#6a45a0"/>
      <polygon points="676,0 880,-12 880,34 676,46" fill="#4c2a80"/>
    </svg>
  </section>

</main>
</body>
</html>
```